Hydraulics Company Business Card Design

Modern business card design for a hydraulics company.
Our company colours are - black, orange and white.
I would like the following contact details included-
Name
Position
Phone number
Email
Website
Street Address

I have attached our company logo.
I would like the back of the card white.

Thank you.

```html
<!DOCTYPE html>
<html lang="en">
<head>
<meta charset="utf-8">
<title>Corrindale Hydraulics – Business Card</title>
<link rel="stylesheet" href="https://fonts.googleapis.com/css2?family=Arimo:wght@400;700&display=swap">
<style>
  :root {
    --backdrop: #2d2d2d;
    --card-black: #000000;
    --card-white: #ffffff;
    --brand-orange: #f7a11d;
    --text-white: #ffffff;
  }
  * { margin: 0; padding: 0; box-sizing: border-box; }
  html, body {
    width: 1200px;
    height: 1015px;
    overflow: hidden;
    background: var(--backdrop);
    font-family: "Arimo", Arial, sans-serif;
  }
  .card-set {
    position: relative;
    width: 1200px;
    height: 1015px;
  }
  .card {
    position: absolute;
    left: 250px;
    width: 700px;
    height: 400px;
    box-shadow: 0 10px 30px rgba(0,0,0,0.45);
    overflow: hidden;
  }
  .card--logo-side { top: 70px; background: var(--card-white); }
  .card--contact-side { top: 540px; background: var(--card-black); }

  .card__rule {
    position: absolute;
    left: 0;
    top: 0;
    width: 700px;
    height: 400px;
    pointer-events: none;
  }

  .wordmark {
    color: var(--brand-orange);
    font-weight: 700;
    line-height: 1;
    letter-spacing: -0.5px;
    white-space: nowrap;
  }
  .card--logo-side .wordmark {
    position: absolute;
    left: 0;
    right: 0;
    top: 130px;
    text-align: center;
    font-size: 50px;
  }
  .card--contact-side .wordmark {
    position: absolute;
    right: 40px;
    top: 92px;
    font-size: 30px;
  }

  .contact {
    position: absolute;
    left: 52px;
    top: 52px;
    color: var(--text-white);
  }
  .contact__name {
    color: var(--brand-orange);
    font-weight: 700;
    font-size: 24px;
    letter-spacing: 0.3px;
  }
  .contact__role {
    font-size: 15px;
    letter-spacing: 0.6px;
    margin-top: 3px;
  }
  .contact__divider {
    width: 140px;
    height: 1px;
    background: var(--brand-orange);
    margin: 18px 0 14px;
  }
  .contact__list { list-style: none; }
  .contact__item {
    display: flex;
    align-items: center;
    gap: 10px;
    font-size: 17px;
    line-height: 26px;
  }
  .contact__icon {
    width: 16px;
    height: 16px;
    flex: none;
  }
  .contact__address {
    font-style: normal;
    font-size: 17px;
    line-height: 24px;
  }
</style>
</head>
<body>
<main class="card-set">
  <section class="card card--logo-side" aria-label="Card logo side">
    <p class="wordmark">Corrindale Hydraulics</p>
    <svg class="card__rule" viewBox="0 0 700 400" aria-hidden="true">
      <path d="M0 352 H310 Q325 352 332 342 Q340 332 355 332 H700" fill="none" stroke="var(--brand-orange)" stroke-width="7"/>
    </svg>
  </section>

  <section class="card card--contact-side" aria-label="Card contact side">
    <div class="contact">
      <p class="contact__name">MARCUS ELLERY</p>
      <p class="contact__role">MANAGING DIRECTOR</p>
      <div class="contact__divider"></div>
      <ul class="contact__list">
        <li class="contact__item">
          <svg class="contact__icon" viewBox="0 0 24 24" aria-hidden="true"><path fill="var(--brand-orange)" d="M6.6 10.8a15.1 15.1 0 0 0 6.6 6.6l2.2-2.2a1 1 0 0 1 1-.25 11.4 11.4 0 0 0 3.6.57 1 1 0 0 1 1 1V20a1 1 0 0 1-1 1A17 17 0 0 1 3 4a1 1 0 0 1 1-1h3.5a1 1 0 0 1 1 1c0 1.25.2 2.45.57 3.57a1 1 0 0 1-.25 1z"/></svg>
          044-987 650 321
        </li>
        <li class="contact__item">
          <svg class="contact__icon" viewBox="0 0 24 24" aria-hidden="true"><rect x="2" y="5" width="20" height="14" fill="var(--brand-orange)"/><path d="M2 5l10 8 10-8" fill="none" stroke="#000" stroke-width="1.6"/></svg>
          hello@corrindale.com
        </li>
        <li class="contact__item">
          <svg class="contact__icon" viewBox="0 0 24 24" aria-hidden="true"><g fill="none" stroke="var(--brand-orange)" stroke-width="2"><circle cx="12" cy="12" r="9.5"/><ellipse cx="12" cy="12" rx="4" ry="9.5"/><path d="M2.5 12h19M4 7h16M4 17h16"/></g></svg>
          www.corrindalehyd.com
        </li>
      </ul>
      <div class="contact__divider"></div>
      <address class="contact__address">17, Harbour Works Road<br>20814,Northland</address>
    </div>
    <p class="wordmark">Corrindale Hydraulics</p>
    <svg class="card__rule" viewBox="0 0 700 400" aria-hidden="true">
      <path d="M0 362 H340 Q355 362 362 352 Q370 342 385 342 H700" fill="none" stroke="var(--brand-orange)" stroke-width="7"/>
    </svg>
  </section>
</main>
</body>
</html>
```